Visitenkarten-Design für Goldankauf und Verkauf von Trauringen
Zielgruppe
Goldankauf und Verkauf von Trauringen
Aufgabenstellung
Edel, nicht zu bunt, das Design soll sich dem Kunden einprägen, ansprechend, gerne können auch Wasserzeichen verwendet werden.

```html
<!DOCTYPE html>
<html lang="de">
<head>
<meta charset="utf-8">
<title>Aurelia – Visitenkarten</title>
<link href="https://fonts.googleapis.com/css2?family=Cinzel:wght@400;600&family=Libre+Baskerville&display=swap" rel="stylesheet">
<style>
  :root {
    --canvas: #ececec;
    --card-dark: #141414;
    --card-mid: #222120;
    --gold: #c9a227;
    --gold-light: #f1d36a;
    --gold-deep: #8a6a12;
    --text-light: #e9e6df;
  }
  * { margin: 0; padding: 0; box-sizing: border-box; }
  html, body {
    width: 1200px; height: 3000px; overflow: hidden;
    background: var(--canvas);
  }
  .sheet {
    position: relative; width: 1200px; height: 3000px;
    display: flex; flex-direction: column; align-items: center; justify-content: center;
    gap: 200px;
  }
  .card {
    position: relative; width: 900px; height: 514px; overflow: hidden;
    background: radial-gradient(ellipse at 40% 35%, var(--card-mid), var(--card-dark) 75%);
    border: 7px solid var(--gold);
    border-image: linear-gradient(120deg, var(--gold-deep), var(--gold-light) 45%, var(--gold) 60%, var(--gold-deep)) 1;
  }
  /* Front */
  .brand {
    position: absolute; left: 0; right: 0; top: 160px;
    display: flex; flex-direction: column; align-items: center;
  }
  .brand-row { display: flex; align-items: center; gap: 26px; }
  .brand-mark {
    width: 44px; height: 44px; background: var(--gold);
  }
  .brand-name {
    font-family: "Cinzel", serif; font-weight: 600; font-size: 92px;
    color: var(--gold); letter-spacing: 4px; line-height: 1;
  }
  .brand-rule {
    width: 520px; height: 2px; margin-top: 18px;
    background: linear-gradient(90deg, transparent, var(--gold) 20%, var(--gold) 80%, transparent);
  }
  .brand-tagline {
    margin-top: 14px;
    font-family: "Cinzel", serif; font-size: 26px; letter-spacing: 3px;
    color: var(--text-light);
  }
  /* Back */
  .contact {
    position: absolute; left: 58px; top: 120px; width: 560px;
  }
  .owner {
    font-family: "Cinzel", serif; font-size: 36px; color: var(--gold);
    letter-spacing: 1px; line-height: 1.1;
  }
  .contact-line {
    font-family: "Libre Baskerville", serif; font-size: 17px;
    color: var(--text-light); line-height: 1.55;
  }
  .contact-mobile { margin-top: 8px; }
  .contact-address { margin-top: 70px; }
  .mark-area {
    position: absolute; right: 0; bottom: 0; width: 240px; height: 330px;
    background: linear-gradient(160deg, rgba(201,162,39,0.55), rgba(138,106,18,0.25) 70%, transparent);
  }
</style>
</head>
<body>
<main class="sheet">
  <section class="card card-front">
    <div class="brand">
      <div class="brand-row">
        <span class="brand-mark"></span>
        <span class="brand-name">Aurelia</span>
      </div>
      <div class="brand-rule"></div>
      <div class="brand-tagline">Goldankauf &amp; Trauringe</div>
    </div>
  </section>

  <section class="card card-back">
    <div class="contact">
      <div class="owner">INH. MARLENE KASTNER</div>
      <div class="contact-line contact-mobile">Mobil: 06120-4418305 · kontakt@aurelia-talheim.de</div>
      <div class="contact-line contact-address">Lindenhofer Gasse 12 · 63450 Talheim</div>
      <div class="contact-line">www.aurelia-talheim.de · kontakt@aurelia-talheim.de</div>
      <div class="contact-line">Tel.: 06120-4418305 · Fax: 06120-4418306</div>
    </div>
    <div class="mark-area" role="img" aria-label="Large gold decorative brand mark area"></div>
  </section>
</main>
</body>
</html>
```